Tidal Fern Business Cards

We need something new, fun and exciting for business cards. Our current ones are just plain and we need a design that pops. We want name, position held, phone, email on the front, and a 20% discount on the back. I have also uploaded our old business cards creative to see what we are not wanting, and how boring they were and we want something jazzed up from this, cool design and catches people attention.

```html
<!DOCTYPE html>
<html lang="en">
<head>
<meta charset="utf-8">
<title>Tidal Fern Business Card</title>
<link rel="stylesheet" href="https://fonts.googleapis.com/css2?family=Roboto:wght@300;400;500;700&display=swap">
<style>
  :root {
    --navy: #1b3d6e;
    --coral: #f2726f;
    --coral-soft: #f9b3a8;
    --white: #ffffff;
    --ink: #1a1a1a;
    --grey-light: #e6e6e6;
    --grey-mid: #a9a9a9;
    --grey-dark: #7d7d7d;
    --page: #ffffff;
  }
  html, body {
    margin: 0;
    padding: 0;
    width: 1200px;
    height: 1200px;
    overflow: hidden;
    background: var(--page);
    font-family: "Roboto", Arial, sans-serif;
  }
  .canvas {
    position: relative;
    width: 1200px;
    height: 1200px;
  }
  .card {
    position: absolute;
    left: 48px;
    top: 371px;
    width: 1097px;
    height: 349px;
    box-shadow: 6px 8px 10px rgba(0, 0, 0, 0.35);
    background: var(--white);
  }
  .front {
    position: absolute;
    left: 0;
    top: 0;
    width: 548px;
    height: 349px;
    background: var(--white);
  }
  .front-bar {
    position: absolute;
    left: 0;
    bottom: 0;
    width: 548px;
    height: 16px;
    background: var(--coral);
  }
  .holder-name {
    position: absolute;
    right: 29px;
    top: 36px;
    margin: 0;
    font-size: 31px;
    font-weight: 400;
    letter-spacing: 0.5px;
    color: var(--navy);
    white-space: nowrap;
  }
  .holder-role {
    position: absolute;
    left: 399px;
    top: 73px;
    width: 149px;
    height: 24px;
    border-radius: 12px 0 0 12px;
    background: var(--coral);
    color: var(--white);
    font-size: 18px;
    font-weight: 300;
    line-height: 24px;
    text-align: right;
    padding-right: 29px;
    box-sizing: border-box;
  }
  .holder-dept {
    position: absolute;
    right: 29px;
    top: 103px;
    font-size: 15px;
    font-weight: 400;
    color: var(--ink);
    white-space: nowrap;
  }
  .divider {
    position: absolute;
    top: 130px;
    width: 2px;
    height: 199px;
    background: var(--coral);
  }
  .divider--a { left: 272px; }
  .divider--b { left: 278px; top: 150px; height: 160px; }
  .brand {
    position: absolute;
    left: 39px;
    top: 160px;
    display: flex;
    align-items: center;
    gap: 10px;
  }
  .brand-dot {
    width: 26px;
    height: 26px;
    border-radius: 50%;
    background: var(--coral);
  }
  .brand-name {
    font-size: 36px;
    font-weight: 500;
    color: var(--navy);
    white-space: nowrap;
  }
  .social {
    position: absolute;
    left: 99px;
    top: 242px;
    display: flex;
    gap: 15px;
  }
  .social-tile {
    width: 27px;
    height: 27px;
    border-radius: 5px;
    background: linear-gradient(160deg, var(--grey-light), var(--grey-dark));
  }
  .contact-note {
    position: absolute;
    left: 39px;
    top: 282px;
    width: 226px;
    margin: 0;
    font-size: 10.5px;
    line-height: 13px;
    color: var(--ink);
    text-align: justify;
  }
  .contact-note strong { font-weight: 700; }
  .contact-list {
    position: absolute;
    left: 299px;
    top: 220px;
    margin: 0;
    padding: 0;
    list-style: none;
  }
  .contact-item {
    display: flex;
    align-items: center;
    gap: 10px;
    height: 19px;
    margin-bottom: 6.5px;
    font-size: 11.5px;
    font-weight: 700;
    color: var(--ink);
  }
  .contact-icon {
    width: 19px;
    height: 19px;
    border-radius: 50%;
    background: radial-gradient(circle at 35% 30%, var(--coral-soft), var(--coral));
    display: flex;
    align-items: center;
    justify-content: center;
  }
  .contact-icon svg { width: 11px; height: 11px; }
  .back {
    position: absolute;
    left: 548px;
    top: 0;
    width: 549px;
    height: 349px;
    background: var(--navy);
    overflow: hidden;
  }
  .back-art {
    position: absolute;
    left: 0;
    top: 0;
    width: 549px;
    height: 349px;
    background: linear-gradient(120deg, var(--navy) 0%, var(--navy) 35%, #6d4f6f 65%, var(--coral) 100%);
  }
  .discount {
    position: absolute;
    left: 88px;
    top: 187px;
    width: 138px;
    height: 138px;
  }
  .discount svg {
    position: absolute;
    left: 0;
    top: 0;
  }
  .discount-value,
  .discount-label {
    position: absolute;
    left: 0;
    width: 138px;
    text-align: center;
    color: var(--white);
    font-weight: 400;
  }
  .discount-value { top: 30px; font-size: 46px; line-height: 50px; }
  .discount-label { top: 80px; font-size: 22px; line-height: 24px; }
</style>
</head>
<body>
<div class="canvas">
  <div class="card">
    <section class="front">
      <h1 class="holder-name">MARLO QUINBY</h1>
      <div class="holder-role">Director</div>
      <div class="holder-dept">Business Devlopment &amp; Research</div>

      <div class="divider divider--a"></div>
      <div class="divider divider--b"></div>

      <div class="brand">
        <span class="brand-dot"></span>
        <span class="brand-name">Tidal Fern</span>
      </div>

      <div class="social" aria-label="Social profiles">
        <span class="social-tile"></span>
        <span class="social-tile"></span>
        <span class="social-tile"></span>
        <span class="social-tile"></span>
      </div>

      <p class="contact-note"><strong>Contact:</strong> Lorem Ipsum is simply dummy text of the printing and typesetting industry. Lorem Ipsum has been the industry's standard dummy</p>

      <ul class="contact-list">
        <li class="contact-item">
          <span class="contact-icon">
            <svg viewBox="0 0 12 12"><rect x="1" y="2.5" width="10" height="7" fill="none" stroke="#1a1a1a" stroke-width="1.2"/><path d="M1 2.5 L6 6.5 L11 2.5" fill="none" stroke="#1a1a1a" stroke-width="1.2"/></svg>
          </span>
          hello@tidalfern.com
        </li>
        <li class="contact-item">
          <span class="contact-icon">
            <svg viewBox="0 0 12 12"><rect x="3.5" y="1" width="5" height="10" rx="1" fill="#1a1a1a"/><rect x="4.5" y="2.5" width="3" height="5" fill="#f9b3a8"/></svg>
          </span>
          0213579246
        </li>
        <li class="contact-item">
          <span class="contact-icon">
            <svg viewBox="0 0 12 12"><rect x="3" y="1" width="6" height="3" fill="#1a1a1a"/><rect x="1" y="4.5" width="10" height="4.5" rx="1" fill="#1a1a1a"/><rect x="3" y="8" width="6" height="3" fill="#f9b3a8" stroke="#1a1a1a" stroke-width="0.8"/></svg>
          </span>
          0213579246
        </li>
        <li class="contact-item">
          <span class="contact-icon">
            <svg viewBox="0 0 12 12"><circle cx="6" cy="6" r="4.8" fill="none" stroke="#1a1a1a" stroke-width="1.1"/><ellipse cx="6" cy="6" rx="2" ry="4.8" fill="none" stroke="#1a1a1a" stroke-width="0.9"/><path d="M1.2 6 H10.8" stroke="#1a1a1a" stroke-width="0.9"/></svg>
          </span>
          www.tidalfern.com
        </li>
      </ul>

      <div class="front-bar"></div>
    </section>

    <section class="back">
      <div class="back-art" role="img" aria-label="Large coral leaf fronds forming a heart on a navy ground"></div>
      <div class="discount">
        <svg width="138" height="138" viewBox="0 0 138 138" aria-hidden="true">
          <defs>
            <linearGradient id="badge-silver" x1="0" y1="0" x2="1" y2="1">
              <stop offset="0" stop-color="#f2f2f2"/>
              <stop offset="0.5" stop-color="#a9a9a9"/>
              <stop offset="1" stop-color="#6f6f6f"/>
            </linearGradient>
          </defs>
          <polygon fill="url(#badge-silver)" points="69,0 74.8,10.3 82.3,1.3 85.5,12.7 94.9,5.6 95.4,17.4 106,12.4 103.7,24 115.3,21.1 110.4,31.9 122.3,31.2 115.1,40.6 126.8,42.2 117.7,49.7 128.7,53.5 118.2,58.9 128,64.8 116.5,68.1 124.6,76 112.9,77.1 119.6,86.9 108.2,85.8 112.8,97.1 102.1,93.8 104.2,105.7 94.7,100.4 93.9,112.5 86,105.2 82.3,116.7 76.4,107.8 69.8,117.9 66.2,107.1 57.4,115.4 55.3,104.3 45.2,109.9 44.8,98.3 33.8,100.8 35.9,89.4 24.6,88.8 28.9,78.4 18.1,74.7 24.3,65.9 14.5,59.4 22.3,52.8 14.1,44.2 23.1,40.1 16.9,29.9 26.6,28.2 22.9,17.1 32.9,17.9 31.8,6.4 41.3,9.5 42.7,0 51.5,6.2 55.4,-3 62.7,5.3"/>
        </svg>
        <div class="discount-value">20%</div>
        <div class="discount-label">Discount</div>
      </div>
    </section>
  </div>
</div>
</body>
</html>
```